The Festival! Poster for an Annual Dance Showcase

We are looking for a dynamic festival/concert style poster for our annual dance showcase featuring at least one image of our dancers and the main information. The main image should be one of the dancers but there can be a collage of the dancers or smaller images around the poster. I have included some reference images but it can vary from them.

Must have this information;
Date - May 22-26
Location - Mabel Corwin Hale Theatre
Tickets - Vondo.bm

Target Market(s)

Parents and people who love dance

Industry/Entity Type

Dance

Font styles to use
Sans Serif

Colors
E54698
E96AAD
F1A4CE
F9D9EA
FCEFF6

Requirements
Must have
• Logo, Date and Location, Picture of Dancer

```html
<!DOCTYPE html>
<html lang="en">
<head>
<meta charset="utf-8">
<title>The Festival – Annual Dance Showcase</title>
<link rel="stylesheet" href="https://fonts.googleapis.com/css2?family=Montserrat:wght@800;900&family=Oswald:wght@400;500;600&display=swap">
<style>
  :root {
    --pink: #e5168f;
    --pink-soft: #e96aad;
    --mint: #c3dcc3;
    --brown: #553f3d;
    --paper: #ffffff;
    --photo-skin: #d9b9a4;
    --photo-coral: #ef8a78;
    --photo-green: #5f8a62;
    --photo-black: #3a3334;
  }
  * { box-sizing: border-box; margin: 0; padding: 0; }
  html, body { width: 841px; height: 1200px; overflow: hidden; background: var(--paper); }
  .poster { position: relative; width: 841px; height: 1200px; background: var(--paper); overflow: hidden; font-family: "Oswald", sans-serif; }

  .backdrop { position: absolute; inset: 0; }

  .photo { position: absolute; border-radius: 40% 40% 30% 30% / 20% 20% 12% 12%; }
  .photo--hero { left: 240px; top: 190px; width: 395px; height: 640px; background: linear-gradient(160deg, var(--photo-coral), #e86a5c 60%, #d8a98f); opacity: .85; }
  .photo--side-1 { left: 28px; top: 82px; width: 188px; height: 322px; background: linear-gradient(170deg, #ead6c6, var(--photo-skin)); }
  .photo--side-2 { left: 60px; top: 456px; width: 172px; height: 316px; background: linear-gradient(170deg, #8a6a5a, var(--photo-green) 45%); }
  .photo--side-3 { left: 26px; top: 856px; width: 250px; height: 300px; background: linear-gradient(170deg, #6f5a55, var(--photo-black) 45%); }

  .brand { position: absolute; left: 250px; top: 120px; transform: rotate(-8deg); transform-origin: left top; display: flex; align-items: center; gap: 14px; }
  .brand__dot { width: 62px; height: 62px; border-radius: 50%; background: var(--pink); flex: none; }
  .brand__name { font-family: "Montserrat", sans-serif; font-weight: 900; color: var(--brown); line-height: .9; }
  .brand__line-1 { display: block; font-size: 62px; letter-spacing: -1px; }
  .brand__line-2 { display: block; font-size: 35px; }

  .dates { position: absolute; left: 628px; top: 548px; transform: rotate(-9deg); transform-origin: left top; }
  .dates__days { font-weight: 600; font-size: 80px; color: var(--brown); line-height: 1; }
  .dates__month { display: inline-block; background: var(--pink); color: #fff; font-size: 32px; font-weight: 500; padding: 2px 12px; margin-left: 14px; }

  .title-the { position: absolute; left: 258px; top: 740px; transform: rotate(-4deg); font-size: 150px; font-weight: 500; color: var(--brown); line-height: 1; letter-spacing: -2px; }

  .annual { position: absolute; left: 284px; top: 912px; width: 86px; height: 256px; background: var(--pink); clip-path: polygon(0 7%, 100% 0, 100% 100%, 0 100%); }
  .annual__text { position: absolute; left: 50%; top: 53%; transform: translate(-50%, -50%) rotate(90deg); color: #fff; font-size: 38px; font-weight: 600; letter-spacing: 10px; white-space: nowrap; }

  .tilted { position: absolute; transform: rotate(-13deg); transform-origin: left top; white-space: nowrap; }
  .festival { left: 376px; top: 900px; font-size: 128px; font-weight: 500; color: var(--pink); line-height: .95; letter-spacing: -2px; }
  .showcase { left: 388px; top: 1024px; width: 430px; background: var(--brown); color: #fff; font-size: 44px; font-weight: 400; line-height: 1.2; padding-left: 34px; }
  .venue { left: 462px; top: 1086px; font-size: 21px; color: var(--brown); }
  .venue__label { color: var(--pink); }
  .tickets { left: 594px; top: 1094px; width: 222px; background: var(--pink); color: #fff; font-size: 25px; padding: 0 10px 0 14px; line-height: 1.35; }
  .tickets b { font-weight: 600; }
</style>
</head>
<body>
<div class="poster">
  <svg class="backdrop" width="841" height="1200" viewBox="0 0 841 1200" aria-hidden="true">
    <defs>
      <linearGradient id="panelGlow" x1="1" y1="0" x2="0.55" y2="0.35">
        <stop offset="0" stop-color="#e5168f"/>
        <stop offset="0.45" stop-color="#e58fb5"/>
        <stop offset="1" stop-color="#c3dcc3"/>
      </linearGradient>
    </defs>
    <polygon points="103,33 813,33 813,1169 372,1169" fill="var(--mint)"/>
    <polygon points="103,33 813,33 813,1169 372,1169" fill="url(#panelGlow)"/>
    <line x1="28" y1="440" x2="192" y2="404" stroke="var(--mint)" stroke-width="4"/>
    <line x1="28" y1="805" x2="222" y2="762" stroke="var(--mint)" stroke-width="4"/>
  </svg>

  <div class="photo photo--side-1" role="img" aria-label="Dancer in a nude gown reaching upward in an arabesque"></div>
  <div class="photo photo--side-2" role="img" aria-label="Dancer in a green two-piece costume in a lyrical pose"></div>
  <div class="photo photo--side-3" role="img" aria-label="Two dancers in black and floral tops posing together"></div>
  <div class="photo photo--hero" role="img" aria-label="Lead dancer in a coral lace costume leaping with one arm raised"></div>

  <div class="brand">
    <span class="brand__dot"></span>
    <span class="brand__name"><span class="brand__line-1">OPEN STRIDE</span><span class="brand__line-2">SCHOOL OF DANCE</span></span>
  </div>

  <div class="dates">
    <div class="dates__days">22-26</div>
    <div class="dates__month">MAY 2025</div>
  </div>

  <div class="title-the">THE</div>

  <div class="annual"><span class="annual__text">ANNUAL</span></div>

  <div class="tilted festival">FESTIVAL</div>
  <div class="tilted showcase">DANCE SHOWCASE</div>
  <div class="tilted venue"><span class="venue__label">LOCATION</span> - MABEL CORWIN HALE THEATRE</div>
  <div class="tilted tickets">TICKETS : <b>VONDO.BM</b></div>
</div>
</body>
</html>
```